'Ormel Property Development' Business Card

Business Card Features:

High Quality (potentially textured) thick card - preference is white textured card

Logo (supplied)

We plan to use the vertical logo as the main logo. But i am happy for people to use either if they find it works better for the design of the card.

The building icon and also the insert to the 'E' is in a metallic finish, i think this should be finished in a metallic embossed or raised style.
Updates

Please note i have attached both a horizontal and Vertical Logo for your reference. We plan to use the vertical logo as the main logo. But i am happy for people to use either if they find it works better for the design of the card.

Please note i am considering having the cards made on stainless steel. This introduces the option of having cut outs in the card and etching or printing for the design. If you have a good concept for this please submit.

http://www.tinquarry.example/black-metal-cards# this is a site that makes the metal cards to offer some direction . . . . Please note i am basic the selection o the best design, if that means normal print cards on paper then this is what i will choose. But there are some great options with the metal. Thanks.

Industry/Entity Type

Building

Requirements
Must have
• Helvetica font to details side of card - logo as supplied to opposite side.

Card Details:

Darrow Pketts
Managing Director

+61 487 263 518
+61 3 6172 4809

PO Box 73
Ferncliff, VIC 3291

darrow@ormel.example

www.ormel.example

```html
<!DOCTYPE html>
<html lang="en">
<head>
<meta charset="utf-8">
<title>Ormel Property Development – Business Card</title>
<link rel="stylesheet" href="https://fonts.googleapis.com/css2?family=Arimo:wght@400;700&display=swap">
<style>
  :root {
    --backdrop: #3a3a3c;
    --backdrop-deep: #1c1c1e;
    --card-black: #141210;
    --card-sheen: #2a2724;
    --ink-silver: #d4d6d8;
    --ink-soft: #b9bbbd;
  }
  * { margin: 0; padding: 0; box-sizing: border-box; }
  html, body { width: 1200px; height: 720px; overflow: hidden; }
  body {
    background: radial-gradient(ellipse at 50% 0%, var(--backdrop) 0%, var(--backdrop-deep) 100%);
    font-family: "Arimo", Helvetica, Arial, sans-serif;
    display: flex; align-items: center; justify-content: center;
  }
  .business-card {
    position: relative;
    width: 880px; height: 530px;
    border-radius: 6px;
    background:
      repeating-linear-gradient(90deg, rgba(255,255,255,0.018) 0 1px, transparent 1px 3px),
      linear-gradient(125deg, var(--card-black) 0%, var(--card-sheen) 45%, var(--card-black) 100%);
    box-shadow: 0 24px 50px rgba(0,0,0,0.55);
    color: var(--ink-silver);
  }
  .brand {
    position: absolute;
    left: 70px; top: 300px;
    display: flex; align-items: center; gap: 16px;
  }
  .brand-mark { width: 24px; height: 24px; background: var(--ink-silver); }
  .brand-name {
    font-weight: 700;
    font-size: 28px;
    color: var(--ink-silver);
  }
  .details {
    position: absolute;
    right: 60px; top: 70px;
    text-align: right;
  }
  .holder-name { font-weight: 700; font-size: 30px; line-height: 34px; }
  .holder-role { font-size: 19px; line-height: 24px; color: var(--ink-soft); }
  .contact-list {
    list-style: none;
    margin-top: 46px;
    font-size: 19px;
    line-height: 30px;
  }
  .contact-list li {
    display: flex; align-items: center; justify-content: flex-end; gap: 10px;
  }
  .contact-icon {
    width: 16px; height: 16px; flex: none;
    fill: none; stroke: var(--ink-silver); stroke-width: 1.6;
  }
  .contact-icon .solid { fill: var(--ink-silver); stroke: none; }
  .contact-list .postal { margin-top: 30px; }
</style>
</head>
<body>
  <article class="business-card">
    <div class="brand">
      <span class="brand-mark"></span>
      <span class="brand-name">Ormel Property Development</span>
    </div>

    <section class="details">
      <p class="holder-name">Darrow Pketts</p>
      <p class="holder-role">Managing Director</p>

      <ul class="contact-list">
        <li>+61 487 263 518
          <svg class="contact-icon" viewBox="0 0 16 16" aria-hidden="true"><rect x="4" y="1" width="8" height="14" rx="1.5"/><line x1="7" y1="12.5" x2="9" y2="12.5"/></svg>
        </li>
        <li>+61 3 6172 4809
          <svg class="contact-icon" viewBox="0 0 16 16" aria-hidden="true"><path class="solid" d="M2 6c0-2 2.5-3 6-3s6 1 6 3l-2.5 1L10 5.5H6L4.5 7z"/><rect class="solid" x="3" y="8" width="10" height="6" rx="1"/></svg>
        </li>
        <li>darrow@ormel.example
          <svg class="contact-icon" viewBox="0 0 16 16" aria-hidden="true"><rect x="1.5" y="3.5" width="13" height="9"/><polyline points="1.5,3.5 8,9 14.5,3.5"/></svg>
        </li>
        <li>www.ormel.example
          <svg class="contact-icon" viewBox="0 0 16 16" aria-hidden="true"><circle cx="8" cy="8" r="6.5"/><ellipse cx="8" cy="8" rx="2.8" ry="6.5"/><line x1="1.5" y1="8" x2="14.5" y2="8"/></svg>
        </li>
        <li class="postal">PO Box 73 Ferncliff, VIC 3291
          <svg class="contact-icon" viewBox="0 0 16 16" aria-hidden="true"><path class="solid" d="M8 1.5 1 8h2v6.5h4V10h2v4.5h4V8h2z"/></svg>
        </li>
      </ul>
    </section>
  </article>
</body>
</html>
```